Premium modern eliquids labels 84.5 x 80 mm

I am looking for modern graphics for the labels of a new eliquid line that will have 4 different types of eliquids. It will have a tobacco one (brown colours maybe), a fruity one (bright colours maybe), a minty one (green colours maybe) and a creamy one (beige colours maybe).
I will need one of them to see how the design is, that design will have to be adapted to the other 3 colours of the label.
The brand logo is attached. I also attached a sample of what is mandatory to write on the label, you can change size, place and font of what is written, the only thing that cannot be reduced is the yellow parts. I attach the bottle that we will use.The size of the label is 84.5 x 80 mm (base x height).

Target Market(s)

vapers

Requirements
Must have
• My project must have one of the labels.

```html
<!DOCTYPE html>
<html lang="it">
<head>
<meta charset="utf-8">
<title>Velluto Vapor – Tobacco label</title>
<link href="https://fonts.googleapis.com/css2?family=Roboto+Condensed:wght@400;700&family=Archivo:wght@800&display=swap" rel="stylesheet">
<style>
  :root{
    --page:#ffffff;
    --leaf-light:#e8861f;
    --leaf-mid:#b9481a;
    --leaf-dark:#3a0f06;
    --ink-light:#ffffff;
    --ink-dark:#1e0f08;
    --badge:#f9c43d;
    --badge-ink:#3b1408;
    --brand:#6cc1e8;
  }
  *{box-sizing:border-box;margin:0;padding:0}
  html,body{width:1200px;height:1200px;overflow:hidden;background:var(--page)}
  .label{
    position:absolute;left:167px;top:190px;width:865px;height:818px;overflow:hidden;
    font-family:"Roboto Condensed",sans-serif;color:var(--ink-light);
  }
  .leaf-photo{
    position:absolute;inset:0;
    background:
      radial-gradient(ellipse 45% 40% at 55% 42%, var(--leaf-light) 0%, transparent 70%),
      radial-gradient(ellipse 70% 65% at 50% 50%, var(--leaf-mid) 0%, #8a2a10 60%, var(--leaf-dark) 100%);
  }
  .ingredients,.instructions{
    position:absolute;font-weight:700;font-size:24px;line-height:25.5px;letter-spacing:-.3px;
    text-shadow:0 1px 2px rgba(0,0,0,.4);
  }
  .ingredients{left:27px;top:26px}
  .instructions{left:689px;top:26px;width:170px}
  .batch{
    position:absolute;left:29px;top:606px;transform-origin:0 0;transform:rotate(-90deg);
    font-size:19px;white-space:nowrap;letter-spacing:-.6px;
  }
  .batch strong{font-weight:700}
  .brand{
    position:absolute;left:233px;top:318px;width:400px;text-align:center;
    font-weight:700;font-size:50px;letter-spacing:2px;color:var(--brand);line-height:1;
  }
  .flavour-name{
    position:absolute;left:200px;top:522px;width:466px;text-align:center;
  }
  .flavour-name .rule{position:absolute;top:22px;height:2px;background:var(--ink-light);width:80px}
  .flavour-name .rule.left{left:53px}
  .flavour-name .rule.right{right:53px}
  .flavour-name h1{
    display:inline-block;font-weight:700;font-size:40px;line-height:42px;letter-spacing:-.5px;
    background:var(--ink-dark);padding:0 4px;
  }
  .flavour-name p{
    display:block;width:max-content;margin:2px auto 0;font-weight:700;font-size:22px;line-height:24px;
    background:var(--ink-dark);padding:0 4px;
  }
  .producer{
    position:absolute;left:27px;top:620px;font-family:"Archivo",sans-serif;font-weight:800;
    font-size:16px;line-height:19px;
  }
  .producer .lead{font-size:18.5px;letter-spacing:1px}
  .net{position:absolute;font-weight:700;font-size:19px}
  .net.center{left:383px;top:741px;width:100px;text-align:center}
  .net.right{left:704px;top:746px;font-size:22px}
  .badge{
    position:absolute;left:705px;background:var(--badge);color:var(--badge-ink);
    font-family:"Archivo",sans-serif;font-weight:800;text-align:center;
  }
  .badge.collect{width:122px;height:38px;font-size:17px;line-height:16px;padding-top:3px}
  .badge.code{width:88px;height:38px;font-size:22px;line-height:38px;letter-spacing:1px}
  .part{position:absolute;left:707px;font-family:"Archivo",sans-serif;font-weight:800;font-size:13px}
  .icons{position:absolute;left:695px;top:668px}
</style>
</head>
<body>
<main class="label">
  <div class="leaf-photo" role="img" aria-label="Close-up photograph of a backlit dry tobacco leaf with dark veins"></div>

  <section class="ingredients">INGREDIENTI:<br>GLICOLE<br>PROPILENICO<br>SOSTANZE<br>AROMATIZZANTI</section>

  <div class="batch">L.SH20 - <strong>001-PES-D.PROD.22-04-2022</strong> D.SC.21-04-2024</div>

  <section class="instructions">ISTRUZIONI D’USO:<br>Agitare bene prima dell’utilizzo. Diluire nelle percentuali consigliate sul nostro sito. Conservare in luogo fresco e asciutto</section>

  <div class="brand">VELLUTO VAPOR</div>

  <div class="flavour-name">
    <span class="rule left"></span><span class="rule right"></span>
    <h1>TOBACCO</h1>
    <p>Premium Eliquid</p>
  </div>

  <address class="producer" style="font-style:normal">
    <span class="lead">PRODOTTO<br>E CONFEZIONATO<br>DA Brenta Lab srl</span><br>
    Via Lanza 18<br>10100 Torino<br>P.i.12345678901<br>Tel. +39 011 5550123<br>info@brentalab.it
  </address>

  <div class="net center">20 ML NET</div>

  <div class="badge collect" style="top:396px">RACCOLTA<br>PLASTICA</div>
  <div class="part" style="top:440px">ETICHETTA</div>
  <div class="badge code" style="top:459px">PAP 5</div>
  <div class="badge collect" style="top:519px">RACCOLTA<br>PLASTICA</div>
  <div class="part" style="top:564px;left:713px">FLACONE</div>
  <div class="badge code" style="top:581px">PET 1</div>

  <svg class="icons" width="140" height="64" viewBox="0 0 140 64" aria-hidden="true">
    <g fill="none" stroke="#fff" stroke-width="3" stroke-linejoin="round">
      <path d="M30 8 L44 32 M40 30 l4 2 l2 -5"/>
      <path d="M40 50 L12 50 M16 46 l-4 4 l4 4"/>
      <path d="M8 42 L22 16 M18 17 l4 -1 l1 5"/>
    </g>
    <g fill="#fff">
      <circle cx="125" cy="6" r="5"/>
      <path d="M119 13 h12 v26 h-3 v22 h-4 v-22 h-2 v22 h-4 z"/>
      <path d="M119 18 l-16 10 l2 3 l14 -8 z"/>
      <path d="M92 34 h20 l-3 28 h-14 z M96 38 l2 20 h8 l2 -20 z" fill-rule="evenodd"/>
      <rect x="99" y="26" width="3" height="3"/><rect x="104" y="30" width="3" height="3"/>
    </g>
  </svg>

  <div class="net right">20 ML NET</div>
</main>
</body>
</html>
```